Website for a financial survey consultancy

WHO WE ARE
We're a niche HR consultancy specialising in salary comparison surveys for the financial asset management industry. We position ourselves as a small, highly responsive organisation with a strong personal relationship with each of our 50+ blue-chip clients.

WHAT WE DO
Our business is 80% surveys (= products), 20% consultancy (= services). The surveys are a set of online products which clients interact with to find the information they are interested in.

WHAT WE WANT
We are completely revising our existing marketing website and need a new up-to-date look and feel for the site. We want you to design 2 web pages
- Home page
- Internal content page

More details below in Must Have Priorities.

REFERENCE SITES
- www.tallowmere.com - nice background image
- www.quimbelt.com - ignoring the animations
- www.palvastro.com
- www.dulmiko.com - clean, fresh, styly but prob not corporate enough
- www.orvettagrove.com - spacious, beautiful, slightly dated tho
- www.plinzer.co.uk - ignore the colours. Like the simplicity, larger font size (although want to stick with sans-serif fonts for main content)

DELIVERABLES
The final designs should be delivered as one or more PSD files with clearly named layers. All design elements and treatments should be separated out, for example use adjustment layers rather than applied (and subsequently irreversible) adjustments, strokes, shading, etc.

WHAT NEXT
I'll be monitoring the contest every day and can respond to questions fast. You can IM me on Skype or MSN.

Reason: Hi folks,

I am extending the deadline to this project as I am travelling this week and therefore will not be able to make a final decision until next Monday. I will try and provide further feedback over the course of this week but I am only going to be online occasionally so be prepared to wait a few days for a reply from me.

Thanks for all the designs so far.

Owen

Target Market(s)

In order of importance, most important first

1. Potential customers - UK & US financial industry HR professionals, short on time. Heard about us already, want to find out more about what we do, confirm relevance for their needs. Core goal - establish credibility: are we properly resourced, will we be around for years to come, are we *real*.

2. Existing customers - UK & US financial industry professionals, short on time, under pressure, want results quickly, minimum faff, expect high quality, slickly presented information. Primary action: login and use surveys.

3. Industry professionals/researchers - probably arriving through blog content, looking to browse and hoover information. Valuable for their ability to spread awareness of who we are amongst their peers.

Industry/Entity Type

Financial

Requirements
Must have
• GENERAL
Style cues - Corporate, professional, financial, stylish, slick, clean, spacious, light
Size - standard 960px grid

NAVIGATION
- [ Home | About us | Surveys | Consulting | Blog ]
- Sub-nav (roll-over dropdown) on About Us, Surveys & Consulting

ALL PAGES
- Site navigation
- Client login (on screen permanently or link to ajaxy in-page pop-up)
- Footer section
- Existing logo (attached)* - this is obviously an important reference point in the design, esp colour

HOME PAGE
- Communicate (link thru to?) survey/consulting split
- Large photo(s)/backdrop (2-3 interchangeable options ideally). Please consider what rights agreement will be necessary for any photos you include in your design.
- Possibly bigger more prominent version of logo
- Strap line/sentence - "Focussed data is the key to success"
- 3 recent blog posts (should look good with and without blog post images)
- Free downloadable PDF research report + supporting blurb

INTERNAL PAGE
- Page title
- Content - typical page will be less than one screenfull
- Level 1 sub-heading
- Level 2 sub-heading
- Bulleted list
- Content supporting image (any image will do - interested in placement, borders (if any), spacing, caption, etc)
- 'Do something' button

* Note: there is some internal debate about this logo at the moment. Some (me) are keen for it to change, some (not me!) are not. If you have an web page design idea/concept that requires an evolution of the logo, go ahead and evolve it. We can explore this further in the design process as necessary, but don't sweat it.
Nice to have
• Values to communicate
- Knowledgeable
- Professional
- Secure
- Personal
- Experienced
- Financial industry specific
- Accurate
- Reliable
Should not have
• - Search box
- Social media links, other than RSS feed button (discrete)

```html
<!DOCTYPE html>
<html lang="en">
<head>
<meta charset="utf-8">
<title>Dravi Consulting — Home</title>
<link rel="stylesheet" href="https://fonts.googleapis.com/css2?family=Arimo:wght@400;700&family=Mr+De+Haviland&display=swap">
<style>
  :root {
    --page-bg: #e4eef4;
    --top-rule: #3b5b72;
    --frame: #ffffff;
    --ink-dark: #14303b;
    --nav-ink: #17262e;
    --panel: rgba(22, 42, 52, 0.88);
    --panel-cap: #000000;
    --tab: #000000;
    --text-light: #ffffff;
    --footer: #264457;
    --footer-fold: #12232d;
    --btn-orange-top: #ffc24a;
    --btn-orange-bottom: #f28a10;
    --btn-green: #3fb12b;
    --pdf-red: #d7262b;
  }
  * { margin: 0; padding: 0; box-sizing: border-box; }
  html, body { width: 1200px; height: 768px; overflow: hidden; }
  body {
    position: relative;
    background: var(--page-bg);
    font-family: "Arimo", Arial, sans-serif;
    color: var(--nav-ink);
  }
  .top-rule { position: absolute; left: 0; top: 0; width: 1200px; height: 3px; background: var(--top-rule); }
  .site-frame {
    position: absolute; left: 75px; top: 3px; width: 1048px; height: 730px;
    background: var(--frame);
    box-shadow: 0 0 18px rgba(40, 70, 90, 0.18);
  }
  .hero-backdrop {
    position: absolute; left: 88px; top: 3px; width: 1024px; height: 730px;
    background:
      linear-gradient(200deg, rgba(255,255,255,0.0) 45%, rgba(20,50,70,0.35) 100%),
      linear-gradient(160deg, #dbe6ec 0%, #b5cbd6 30%, #6f97b0 60%, #2f5d7c 85%, #1f3e52 100%);
  }
  .brand { position: absolute; left: 103px; top: 13px; width: 128px; }
  .brand-square { width: 128px; height: 124px; background: var(--ink-dark); }
  .brand-name {
    display: block; margin-top: 10px; text-align: center;
    font-size: 42px; font-weight: 400; color: var(--ink-dark); letter-spacing: 1px;
  }
  .main-nav, .footer-nav { position: absolute; display: flex; font-size: 15px; }
  .main-nav { right: 116px; top: 22px; color: var(--nav-ink); }
  .main-nav a, .footer-nav a { color: inherit; text-decoration: none; }
  .main-nav .sep, .footer-nav .sep { margin: 0 13px; }
  .strapline {
    position: absolute; left: 270px; top: 96px;
    font-family: "Mr De Haviland", cursive; font-size: 38px; color: #0d1a20;
    white-space: nowrap;
  }
  .strap-swash { position: absolute; left: 430px; top: 130px; }
  .info-panel {
    position: absolute; left: 717px; top: 83px; width: 338px; height: 644px;
    background: var(--panel); border-top: 7px solid var(--panel-cap);
  }
  .panel-tab {
    position: absolute; left: 709px; width: 262px; height: 32px;
    background: var(--tab); color: var(--text-light);
    font-size: 21px; line-height: 32px; padding-left: 34px; font-weight: 400;
  }
  .panel-copy {
    position: absolute; left: 744px; width: 285px;
    color: var(--text-light); font-size: 13.4px; line-height: 18px;
  }
  .slide-arrow { position: absolute; top: 560px; }
  .slide-arrow.prev { left: 97px; }
  .slide-arrow.next { left: 1058px; }
  .report-cta { position: absolute; left: 406px; top: 580px; }
  .report-label {
    position: absolute; left: 487px; top: 631px; width: 150px;
    text-align: center; color: #1a1a1a; line-height: 18px;
  }
  .report-label .small { display: block; font-size: 14.5px; }
  .report-label .big { display: block; font-size: 17px; }
  .footer-band { position: absolute; left: 61px; top: 658px; }
  .footer-nav { left: 119px; top: 732px; color: var(--text-light); font-size: 14px; }
  .copyright { position: absolute; left: 935px; top: 743px; font-size: 11px; color: var(--text-light); letter-spacing: 0.3px; }
</style>
</head>
<body>
  <div class="top-rule"></div>
  <div class="site-frame"></div>
  <div class="hero-backdrop" role="img" aria-label="Photograph looking up at a curved glass office tower against a pale blue sky"></div>

  <div class="brand">
    <div class="brand-square"></div>
    <span class="brand-name">Dravi</span>
  </div>

  <nav class="main-nav">
    <a href="#">Home</a><span class="sep">/</span>
    <a href="#">About us</a><span class="sep">/</span>
    <a href="#">Surveys</a><span class="sep">/</span>
    <a href="#">Consulting</a><span class="sep">/</span>
    <a href="#">Blog</a>
  </nav>

  <p class="strapline">Focussed data is the key to success</p>
  <svg class="strap-swash" width="290" height="16" viewBox="0 0 290 16">
    <path d="M5 14 C 90 4, 200 2, 285 10" fill="none" stroke="#1a2328" stroke-width="1.2"/>
  </svg>

  <section class="info-panel" aria-label="Company and blog"></section>

  <h2 class="panel-tab" style="top:106px">Company</h2>
  <p class="panel-copy" style="top:146px">Dravi Consulting specialises in compensa-tion strategy and benchmarking, designing performance management/reward systems and HR solutions in asset management. Our unique approach is characterised by senior HR professionals with extensive experience who provide practical HR advice, and deliver reward and performance solutions on time and within budget.</p>

  <h2 class="panel-tab" style="top:347px">Recent Blog Posts</h2>
  <p class="panel-copy" style="top:388px">Dravi Consulting specialises in compensa-tion strategy and benchmarking, designing performance management/reward systems and HR solutions in asset management.</p>
  <p class="panel-copy" style="top:496px">Dravi Consulting specialises in compensa-tion strategy and benchmarking, designing performance management/reward systems and HR solutions in asset management.</p>
  <p class="panel-copy" style="top:604px">Dravi Consulting specialises in compensa-tion strategy and benchmarking, designing performance management/reward systems and HR solutions in asset management.</p>

  <svg class="slide-arrow prev" width="44" height="44" viewBox="0 0 44 44" aria-label="Previous slide">
    <circle cx="22" cy="22" r="21" fill="#000" stroke="#fff" stroke-width="1.5"/>
    <path d="M26 12 L15 22 L26 32" fill="none" stroke="#fff" stroke-width="5" stroke-linejoin="round"/>
  </svg>
  <svg class="slide-arrow next" width="44" height="44" viewBox="0 0 44 44" aria-label="Next slide">
    <circle cx="22" cy="22" r="21" fill="#000" stroke="#fff" stroke-width="1.5"/>
    <path d="M18 12 L29 22 L18 32" fill="none" stroke="#fff" stroke-width="5" stroke-linejoin="round"/>
  </svg>

  <svg class="footer-band" width="1075" height="110" viewBox="0 0 1075 110">
    <polygon points="0,17 14,3 14,17" fill="var(--footer-fold)"/>
    <polygon points="1059,59 1073,68 1059,68" fill="var(--footer-fold)"/>
    <polygon points="0,17 1073,68 1073,110 0,110" fill="var(--footer)"/>
  </svg>

  <svg class="report-cta" width="270" height="112" viewBox="0 0 270 112" aria-label="Download research report">
    <defs>
      <linearGradient id="pill" x1="0" y1="0" x2="0" y2="1">
        <stop offset="0" stop-color="var(--btn-orange-top)"/>
        <stop offset="1" stop-color="var(--btn-orange-bottom)"/>
      </linearGradient>
      <radialGradient id="knob" cx="0.4" cy="0.35" r="0.7">
        <stop offset="0" stop-color="#8be06c"/>
        <stop offset="1" stop-color="var(--btn-green)"/>
      </radialGradient>
    </defs>
    <rect x="34" y="43" width="212" height="56" rx="28" fill="url(#pill)" stroke="#d8dde0" stroke-width="2"/>
    <circle cx="37" cy="71" r="36" fill="#3a3f42"/>
    <circle cx="37" cy="71" r="31" fill="#c9cfd2"/>
    <circle cx="37" cy="71" r="27" fill="url(#knob)"/>
    <path d="M29 56 H45 V70 H54 L37 87 L20 70 H29 Z" fill="#fff"/>
    <g transform="translate(214 1)">
      <path d="M0 0 H42 L50 8 V64 H0 Z" fill="#fff" stroke="#c8c8c8"/>
      <rect x="0" y="0" width="42" height="22" fill="var(--pdf-red)"/>
      <text x="5" y="16" font-family="Arimo, sans-serif" font-size="12" font-weight="700" fill="#fff">PDF</text>
      <rect x="6" y="28" width="22" height="2" fill="#bbb"/>
      <rect x="6" y="34" width="26" height="2" fill="#bbb"/>
      <rect x="6" y="40" width="20" height="2" fill="#bbb"/>
      <rect x="28" y="38" width="18" height="22" fill="#f2b8c0"/>
    </g>
  </svg>
  <p class="report-label"><span class="small">Collect your Free</span><span class="big">Research Report</span></p>

  <nav class="footer-nav">
    <a href="#">Home</a><span class="sep">/</span>
    <a href="#">About us</a><span class="sep">/</span>
    <a href="#">Surveys</a><span class="sep">/</span>
    <a href="#">Consulting</a><span class="sep">/</span>
    <a href="#">Blog</a>
  </nav>
  <p class="copyright">Copyright 2011. All rights reserved.</p>
</body>
</html>
```